Website redesign

Looking to redesign our existing website. (hire4ward.com.au)
New design needs to be bright, fun and have an easy flowing.
The website needs to be design with call to action.

Some examples of other websites:
brightdesk.com
lendnest.com.au

We are happy with the content of our existing website.

Target Market(s)

other businesses

Industry/Entity Type

Business Service

Number of Pages Required

5+ page

Requirements
Must have
• Theme redesign
Cool animation similar to brightdesk.com

```html
<!DOCTYPE html>
<html lang="en">
<head>
<meta charset="utf-8">
<title>Hire 4 Ward — Virtual Assistants</title>
<link href="https://fonts.googleapis.com/css2?family=Open+Sans:wght@400;600;700&display=swap" rel="stylesheet">
<style>
:root{
  --blue:#17a6e3;
  --blue-dark:#0d8fcf;
  --ink:#1c1c1c;
  --text:#3a3a3a;
  --page:#f4f4f4;
  --process:#e2effc;
  --footer:#12a9e1;
  --white:#ffffff;
  --line:#8a8a8a;
}
*{box-sizing:border-box;margin:0;padding:0}
html,body{width:1200px;height:4021px;overflow:hidden}
body{font-family:"Open Sans",Arial,sans-serif;background:var(--page);color:var(--text);position:relative}
.abs{position:absolute}
.btn{position:absolute;display:flex;align-items:center;justify-content:center;font-size:13px;font-weight:700;border-radius:2px;text-decoration:none}
.btn-solid{background:var(--blue);color:var(--white)}
.btn-outline{border:2px solid var(--blue);color:var(--blue);background:transparent}
.btn-white{background:var(--white);color:var(--blue)}

/* header */
.brand{left:150px;top:14px;color:var(--ink);font-weight:700;line-height:1}
.brand .mark{font-size:24px}
.brand .name{font-size:11px;font-weight:600;margin-top:4px;letter-spacing:.2px}
.nav a{position:absolute;top:24px;font-size:12px;font-weight:600;color:var(--ink);text-decoration:none;letter-spacing:.3px}
.nav a.active{color:var(--blue)}
.nav .underline{position:absolute;left:743px;top:57px;width:76px;height:2px;background:var(--blue)}
.call{left:938px;top:14px;width:112px;height:34px;flex-direction:column;font-size:11px;line-height:1.1;font-weight:600}

/* hero */
.hero-visual{left:730px;top:78px;width:470px;height:500px;border-radius:250px 0 0 250px;background:radial-gradient(circle at 45% 50%,#9fd8f3 0%,#4fb6e6 55%,#2a8fc4 100%)}
.hero-kicker{left:150px;top:222px;font-size:41px;font-weight:600;color:var(--blue);letter-spacing:-.3px}
.hero-title{left:148px;top:267px;font-size:41px;font-weight:700;color:var(--ink);letter-spacing:-.5px}
.hero-list{left:150px;top:330px;list-style:none;font-size:20px;color:var(--ink);line-height:23.5px}
.hero-list li{display:flex;align-items:center;gap:10px}
.hero-call{left:179px;top:412px;width:111px;height:33px}

/* intro */
.intro-kicker{left:149px;top:658px;font-size:28px;font-weight:600;color:var(--blue)}
.intro-title{left:150px;top:690px;font-size:29px;line-height:33px;color:var(--ink)}
.intro-copy{left:150px;top:772px;width:540px;font-size:13px;line-height:27px;color:var(--text)}
.intro-btn{left:359px;top:864px;width:111px;height:32px}
.video{left:727px;top:665px;width:323px;height:182px;border-radius:4px;background:linear-gradient(135deg,#2a5d86,#17324a);box-shadow:0 3px 8px rgba(0,0,0,.3);overflow:hidden}
.video .vtitle{position:absolute;left:52px;top:16px;color:#fff;font-size:14px}
.video .vdot{position:absolute;left:12px;top:12px;width:30px;height:30px;border-radius:50%;background:#fff;opacity:.85}
.video .play{position:absolute;left:132px;top:76px;width:58px;height:38px;border-radius:9px;background:#212121;display:flex;align-items:center;justify-content:center}

/* process */
.process{left:0;top:941px;width:1200px;height:1775px;background:var(--process)}
.section-title{position:absolute;width:100%;text-align:center;font-size:28px;font-weight:600;color:var(--blue)}
.step h3{position:absolute;font-size:22px;font-weight:600;color:var(--ink);letter-spacing:.6px}
.step p{position:absolute;font-size:13px;line-height:19.5px;color:var(--text)}
.illus{position:absolute}
.illus-a{background:linear-gradient(160deg,#a5e6f5 0%,#f4a3a3 70%,#f2c4dc 100%)}
.illus-b{background:linear-gradient(160deg,#f79b9b 0%,#e6f1bd 60%,#fde4b3 100%)}
.illus-c{background:linear-gradient(160deg,#f79b9b 0%,#f0f5c4 45%,#f2c4dc 100%)}
.illus-d{background:linear-gradient(160deg,#a5e6f5 0%,#d5f0f7 60%,#f2c4dc 100%)}
.illus-e{background:linear-gradient(160deg,#f79b9b 0%,#a5e6f5 50%,#f2c4dc 100%)}
.learn{left:529px;top:2637px;width:142px;height:33px}

/* services */
.services{left:0;top:2716px;width:1200px;height:464px;background:linear-gradient(120deg,#2ea7de 0%,#4bb7e6 50%,#2b9cd4 100%)}
.services .section-title{color:var(--white);top:38px}
.services-lead{left:175px;top:96px;font-size:16px;line-height:22px;font-weight:700;color:var(--white)}
.services-list{left:599px;top:100px;list-style:none;color:var(--white);font-size:13px}
.services-list li{display:flex;align-items:center;gap:12px;height:34px}
.services-more{left:529px;top:246px;width:142px;height:31px}
.services-cta{left:0;top:296px;width:1200px;text-align:center;color:var(--white);font-size:21px;line-height:28px}

/* quote */
.quote{left:150px;top:3113px;width:900px;height:417px;background:var(--process);box-shadow:0 3px 10px rgba(0,0,0,.18)}
.quote .section-title{top:8px}
.quote .sub{position:absolute;width:100%;top:42px;text-align:center;font-size:15px;color:var(--ink)}
.field{position:absolute;border-bottom:1px solid var(--line);font-size:12px;color:#666;padding:0 6px 6px}
.check{left:46px;top:312px;font-size:12px;color:var(--ink);display:flex;align-items:center;gap:6px}
.check span.box{width:10px;height:10px;border:1px solid #444;border-radius:50%}
.submit{left:39px;top:337px;width:142px;height:31px}

/* why */
.why .section-title{top:3566px}
.why-sub{left:0;top:3600px;width:1200px;text-align:center;font-size:15px;color:var(--ink)}
.why-item{position:absolute;display:flex;align-items:center;gap:9px;font-size:15px;color:var(--ink)}
.why-btn{left:529px;top:3704px;width:142px;height:33px}

/* footer */
.footer{left:0;top:3781px;width:1200px;height:240px;background:var(--footer);color:var(--white)}
.footer .fmark{position:absolute;left:150px;top:52px;font-size:40px;font-weight:700;line-height:1}
.footer .fname{position:absolute;left:150px;top:98px;font-size:11px;font-weight:600}
.footer .ftag{position:absolute;left:150px;top:122px;font-size:11px}
.footer .fcopy{position:absolute;left:150px;top:152px;font-size:9px;opacity:.9}
.footer .fcredit{position:absolute;left:150px;top:182px;font-size:9px}
</style>
</head>
<body>

<!-- header -->
<div class="abs brand"><div class="mark">H4</div><div class="name">HIRE 4 WARD</div></div>
<nav class="nav">
  <a style="left:400px">HOME</a>
  <a style="left:482px">OUR STORY</a>
  <a style="left:598px">TIPS AND TRICKS</a>
  <a class="active" style="left:743px">CONTACT US</a>
  <a style="left:866px">FAQ</a>
  <span class="underline"></span>
</nav>
<a class="btn btn-solid call"><span>CALL US</span><span>07 5550 1234</span></a>

<!-- hero -->
<div class="abs hero-visual" role="img" aria-label="Hero photograph of a laptop keyboard in blue tones"></div>
<div class="abs hero-kicker">VIRTUAL ASSISTANT?</div>
<div class="abs hero-title">MORE LIKE VALUABLE ASSET!</div>
<ul class="abs hero-list">
  <li><svg width="18" height="14" viewBox="0 0 18 14"><path d="M2 7l5 5 9-10" fill="none" stroke="#17a6e3" stroke-width="3"/></svg>Tech nerds on standby for setup, support and comms!</li>
  <li><svg width="18" height="14" viewBox="0 0 18 14"><path d="M2 7l5 5 9-10" fill="none" stroke="#17a6e3" stroke-width="3"/></svg>One invoice a month - no sneaky Super or TAX!</li>
  <li><svg width="18" height="14" viewBox="0 0 18 14"><path d="M2 7l5 5 9-10" fill="none" stroke="#17a6e3" stroke-width="3"/></svg>Full-time Virtual Assistant betrothed to your business!</li>
</ul>
<a class="btn btn-solid hero-call">07 5550 1234</a>

<!-- intro -->
<div class="abs intro-kicker">OUTSOURCING</div>
<div class="abs intro-title">A big word that means<br>big things for your business.</div>
<p class="abs intro-copy">Virtual Assistants are the superheroes of the modern office. They can do everything your team can do on a computer at a fraction of the price! (Well, maybe not high five you when you've had a win, but a virtual high five is definitely on the table!)</p>
<a class="btn btn-outline intro-btn">Get Started</a>
<div class="abs video" role="img" aria-label="Video thumbnail showing two team members in an office">
  <span class="vdot"></span>
  <span class="vtitle">Introduction to Hire 4 Ward…</span>
  <span class="play"><svg width="16" height="18" viewBox="0 0 16 18"><path d="M2 1l13 8-13 8z" fill="#fff"/></svg></span>
</div>

<!-- process -->
<section class="abs process">
  <h2 class="section-title" style="top:38px">The Process</h2>

  <div class="step">
    <div class="illus illus-a" style="left:211px;top:111px;width:268px;height:267px" role="img" aria-label="Illustration of a certificate with an award ribbon"></div>
    <h3 style="left:546px;top:148px">Provide Your Preferred Qualifications</h3>
    <p style="left:546px;top:190px;width:450px">Set up a call with our team to specify the requirements and qualifications you're searching for in a Virtual Assistant. This will be our checklist for your perfect assistant! From there, we'll take care of shortlisting, testing, background checking and recruiting.</p>
  </div>

  <div class="step">
    <h3 style="left:209px;top:490px">Endorsing the Shortlisted Candidates</h3>
    <p style="left:211px;top:531px;width:450px">After the thorough vetting process, we'll put forward the best candidate. You can then conduct the final interview on your preferred communication platform at a time that suits you. Once the schedule is set, we'll let the candidates know!</p>
    <div class="illus illus-b" style="left:746px;top:424px;width:244px;height:266px" role="img" aria-label="Illustration of a shield with a person icon"></div>
  </div>

  <div class="step">
    <div class="illus illus-c" style="left:211px;top:737px;width:262px;height:262px" role="img" aria-label="Illustration of two people with speech bubbles"></div>
    <h3 style="left:546px;top:793px">Conducting the Final Interview</h3>
    <p style="left:546px;top:836px;width:450px">The final interview is the perfect time to get to know the candidates. It'll help to have a list of questions prepared that will help you pick out the chosen one!</p>
  </div>

  <div class="step">
    <h3 style="left:242px;top:1124px">Setting up the Tools</h3>
    <p style="left:243px;top:1167px;width:435px">Once you've chosen your Virtual Assistant, it's time for their system to be set up. You can get your own IT team onto the installation, otherwise, we've got a super team of tech peeps who can do it for you.</p>
    <div class="illus illus-d" style="left:707px;top:1044px;width:283px;height:295px" role="img" aria-label="Illustration of a gear connected to a network of boxes"></div>
  </div>

  <div class="step">
    <div class="illus illus-e" style="left:211px;top:1384px;width:267px;height:267px" role="img" aria-label="Illustration of a rocket launching"></div>
    <h3 style="left:546px;top:1455px">Your Magical Journey Begins</h3>
    <p style="left:546px;top:1497px;width:450px">Now you and your Virtual Assistant are all set up and ready to rumble! Feel the magic of having a reliable assistant to take on all the menial, repetitive, time-consuming tasks, and focus your energy on more important things. Meet new clients, explore business opportunities, or just spend some time with friends and family!</p>
  </div>
</section>
<a class="btn btn-solid learn">Learn More</a>

<!-- services -->
<section class="abs services" role="img" aria-label="Background photograph of a team meeting with blue overlay">
  <h2 class="section-title">Our Services</h2>
  <div class="abs services-lead">We'll help you save tens (or even hundreds!)<br>of thousands of dollars per year.<br>But what do WE actually do?<br>GLAD YOU ASKED!</div>
  <ul class="abs services-list">
    <li><svg width="24" height="24" viewBox="0 0 24 24"><circle cx="12" cy="12" r="8" fill="none" stroke="#fff" stroke-width="6" stroke-dasharray="4 2.3"/><circle cx="12" cy="12" r="6" fill="#fff"/><circle cx="12" cy="12" r="3" fill="#3aaee2"/></svg>We recruit Virtual Assistants (a.k.a office legends!)</li>
    <li><svg width="24" height="24" viewBox="0 0 24 24"><circle cx="12" cy="12" r="8" fill="none" stroke="#fff" stroke-width="6" stroke-dasharray="4 2.3"/><circle cx="12" cy="12" r="6" fill="#fff"/><circle cx="12" cy="12" r="3" fill="#3aaee2"/></svg>Provide the tech support for these superheroes!</li>
    <li><svg width="24" height="24" viewBox="0 0 24 24"><circle cx="12" cy="12" r="8" fill="none" stroke="#fff" stroke-width="6" stroke-dasharray="4 2.3"/><circle cx="12" cy="12" r="6" fill="#fff"/><circle cx="12" cy="12" r="3" fill="#3aaee2"/></svg>Set up the phone system (their own Hotline!)</li>
    <li><svg width="24" height="24" viewBox="0 0 24 24"><circle cx="12" cy="12" r="8" fill="none" stroke="#fff" stroke-width="6" stroke-dasharray="4 2.3"/><circle cx="12" cy="12" r="6" fill="#fff"/><circle cx="12" cy="12" r="3" fill="#3aaee2"/></svg>We manage Virtual Assistants and keep them in tip-top shape!</li>
  </ul>
  <a class="btn btn-white services-more">Read More</a>
  <p class="abs services-cta"><b>See?</b> It's that simple! <b>The only thing to do now is to finally<br>get started on the quote...</b> just scroll down a little more.</p>
</section>

<!-- quote -->
<section class="abs quote">
  <h2 class="section-title">Get A Quote</h2>
  <p class="sub">Fill in the form below to get a Quote for your own personal Virtual Assistant</p>
  <div class="field" style="left:39px;top:81px;width:822px">Business Name</div>
  <div class="field" style="left:39px;top:128px;width:323px">Your First Name</div>
  <div class="field" style="left:538px;top:128px;width:323px">Your Surname</div>
  <div class="field" style="left:39px;top:181px;width:323px">Contact Number</div>
  <div class="field" style="left:538px;top:181px;width:323px">Email</div>
  <div class="field" style="left:39px;top:234px;width:822px;height:65px">Describe the tasks you'll need from your Virtual Assistant</div>
  <div class="abs check"><span class="box"></span>Subscribe to our newsletter</div>
  <a class="btn btn-solid submit">Submit</a>
</section>

<!-- why -->
<section class="why">
  <h2 class="section-title" style="left:0">It's Time to Hire 4 Ward</h2>
  <p class="abs why-sub">Why are we your new best outsourcing friend?</p>
  <div class="why-item" style="left:218px;top:3637px"><svg width="14" height="12" viewBox="0 0 14 12"><path d="M1 6l4 4 8-9" fill="none" stroke="#17a6e3" stroke-width="2.5"/></svg>Your Own Virtual Assistant</div>
  <div class="why-item" style="left:218px;top:3661px"><svg width="14" height="12" viewBox="0 0 14 12"><path d="M1 6l4 4 8-9" fill="none" stroke="#17a6e3" stroke-width="2.5"/></svg>No Super or TAX</div>
  <div class="why-item" style="left:479px;top:3637px"><svg width="14" height="12" viewBox="0 0 14 12"><path d="M1 6l4 4 8-9" fill="none" stroke="#17a6e3" stroke-width="2.5"/></svg>One Invoice Per Month</div>
  <div class="why-item" style="left:479px;top:3661px"><svg width="14" height="12" viewBox="0 0 14 12"><path d="M1 6l4 4 8-9" fill="none" stroke="#17a6e3" stroke-width="2.5"/></svg>Dedicated Phone System</div>
  <div class="why-item" style="left:730px;top:3634px"><svg width="14" height="12" viewBox="0 0 14 12"><path d="M1 6l4 4 8-9" fill="none" stroke="#17a6e3" stroke-width="2.5"/></svg>Dedicated To Your Business Only</div>
  <div class="why-item" style="left:730px;top:3661px"><svg width="14" height="12" viewBox="0 0 14 12"><path d="M1 6l4 4 8-9" fill="none" stroke="#17a6e3" stroke-width="2.5"/></svg>IT Setup and Support</div>
  <a class="btn btn-outline why-btn">Get Started</a>
</section>

<!-- footer -->
<footer class="abs footer">
  <div class="fmark">H4</div>
  <div class="fname">HIRE 4 WARD</div>
  <div class="ftag">Virtual Assistant? More Like Valuable Asset!</div>
  <div class="fcopy">© 2019 HIRE 4 WARD &nbsp;|&nbsp; ALL RIGHTS RESERVED.</div>
  <div class="fcredit">Website Designed and Hosted by <b>NORTHFIELD STUDIO - WEB DESIGN</b></div>
</footer>

</body>
</html>
```